San Antonio Texas Based Law Firm Needs Eye Catching Professional website

The Calloway Law Firm, PLLC is in need of a fresh, eye catching website that makes the small firm look and appear as professional, organized and innovative as possible.

The Firm wants to highlight its expertise in three main areas.
Estate Planning, Insurance and Mediation.

It is a small firm - but growing, so I am looking for the website to have the appearance not of a small firm - but more of the appearance of a leading national firm. The firm was built after obtaining extensive experience working in both private practice and at two Meridian 400 companies.

The firm was formed based on strong relationships and reputation in the industries the Firm serves and and in the local communities.

My logo, which was designed by pixel forge is clever and something I want to make prominent and build from.

Industry/Entity Type

Legal

Coding

Coded - Design and coding required

Number of Pages Required

3 page

Colors
ffffff
000000

Requirements
Must have
• Very good quality pictures.
• Very organized.
• Easy to navigate.
• A contact Us Page.
• On the Estate Planning page, a place for an upcoming seminar sign up - where we
• would get potential client information to mail out confirmation.
• A way to have people subscribe to periodic updates.
• Link to The Calloway Law Firm Chatterly
• A way to download vcard.
Should not have
• Any pictures of gavels, pillars or other common pictures related to law. (Too boring)

```html
<!DOCTYPE html>
<html lang="en">
<head>
<meta charset="utf-8">
<title>The Calloway Law Firm, PLLC</title>
<link rel="stylesheet" href="https://fonts.googleapis.com/css2?family=Prata&family=Lato:ital,wght@0,400;0,700;1,400&display=swap">
<style>
:root{
  --black:#000000;
  --white:#ffffff;
  --ink:#1c1c1c;
  --text:#2b2b2b;
  --rule:#bdbdbd;
  --dark-2:#333333;
  --pill:#d4d4d4;
  --serif:"Prata", Georgia, serif;
  --sans:"Lato", Arial, sans-serif;
}
*{box-sizing:border-box;margin:0;padding:0}
html,body{width:1200px;height:2293px;overflow:hidden}
body{position:relative;background:var(--white);font-family:var(--sans);color:var(--text)}
.abs{position:absolute}

/* header */
.site-header{position:absolute;left:0;top:0;width:1200px;height:130px;background:var(--black)}
.brand{position:absolute;left:40px;top:44px;width:200px;text-align:center;color:var(--white);font-family:var(--serif);font-size:15px;letter-spacing:1px;line-height:1.3}
.vcard-btn{position:absolute;left:821px;top:18px;width:145px;height:34px;border-radius:17px;background:var(--pill);color:var(--ink);font-family:var(--serif);font-size:11px;display:flex;align-items:center;padding-left:16px;white-space:nowrap}
.vcard-btn svg{position:absolute;right:6px;top:5px}
.header-phone{position:absolute;left:983px;top:17px;display:flex;align-items:center;gap:10px;color:var(--white);font-family:var(--sans);font-size:17px}
.icon-ring{width:35px;height:35px;border-radius:50%;border:2px solid var(--white);display:flex;align-items:center;justify-content:center}
.main-nav{position:absolute;top:84px;left:0;width:1200px;font-family:var(--serif);font-size:15px;color:var(--white)}
.main-nav span{position:absolute;white-space:nowrap}
.main-nav .active::after{content:"";position:absolute;left:0;right:0;top:25px;height:2px;background:var(--white)}

/* hero */
.hero{position:absolute;left:0;top:130px;width:1200px;height:471px;background:linear-gradient(180deg,#3f7fb5 0%,#8fb3cf 42%,#e9c58a 62%,#8a7556 80%,#3a332c 100%)}
.hero-title{position:absolute;left:98px;top:195px;color:var(--white);font-family:var(--serif);font-weight:400;font-size:28px;line-height:39px;text-shadow:0 1px 3px rgba(0,0,0,.5)}
.hero-arrow{position:absolute;top:196px;width:34px;height:80px;background:rgba(255,255,255,.55)}
.hero-arrow.prev{left:0;clip-path:polygon(0 0,100% 50%,0 100%)}
.hero-arrow.next{right:0;clip-path:polygon(100% 0,0 50%,100% 100%)}

/* welcome */
.welcome{position:absolute;left:0;top:601px;width:1200px;height:328px;background:linear-gradient(135deg,#fafafa,#e8e8e8 50%,#f6f6f6)}
.section-title{position:absolute;left:0;width:1200px;text-align:center;font-family:var(--serif);font-weight:400;font-size:31px;color:var(--ink)}
.section-title small{font-size:17px}
.divider{position:absolute;height:1px;background:var(--rule)}
.welcome p{position:absolute;left:138px;top:148px;width:924px;text-align:center;font-size:16.5px;line-height:27px;color:var(--text)}
.btn-more{position:absolute;left:517px;top:252px;width:167px;height:38px;border-radius:19px;background:#2a2a2a;color:var(--white);font-family:var(--serif);font-size:13px;display:flex;align-items:center;padding-left:27px}
.btn-more .chev{position:absolute;right:6px;top:5px;width:28px;height:28px;border-radius:50%;background:var(--white);display:flex;align-items:center;justify-content:center}

/* expertise */
.expertise{position:absolute;left:0;top:929px;width:1200px;height:646px;background:linear-gradient(135deg,#2e2e2e,#1d1d1d 50%,#2b2b2b)}
.expertise .section-title{color:var(--white);top:62px}
.expertise .divider{background:#8a8a8a}
.service{position:absolute;top:175px;width:260px;text-align:center;color:var(--white)}
.service-photo{width:260px;height:208px;border:3px solid var(--white)}
.service h3{font-family:var(--serif);font-weight:400;font-size:20px;line-height:26px;margin-top:30px;height:60px}
.service p{font-size:16px;line-height:22px;margin:6px auto 0;width:215px;color:#e6e6e6;height:90px}
.plus{width:24px;height:24px;border-radius:50%;background:#d9d9d9;margin:17px auto 0;display:flex;align-items:center;justify-content:center}

/* results + testimonials */
.proof{position:absolute;left:0;top:1575px;width:1200px;height:422px;background:linear-gradient(135deg,#f7f7f7,#e6e6e6 55%,#f4f4f4)}
.col-head{position:absolute;top:76px;display:flex;align-items:center;gap:12px;font-family:var(--serif);font-size:26px;color:var(--ink)}
.pager{position:absolute;top:81px;display:flex;gap:8px}
.pager span{width:28px;height:26px;border:1px solid #bbb;background:var(--white);display:flex;align-items:center;justify-content:center}
.results-text{position:absolute;left:52px;top:150px;width:540px;font-size:16.5px;line-height:30px;color:var(--ink)}
.testimonial{position:absolute;left:639px;top:150px;width:510px;height:190px}
.testimonial svg{position:absolute;left:0;top:0}
.quote-mark{position:absolute;left:24px;top:6px;font-family:var(--serif);font-size:48px;color:#bdbdbd}
.testimonial p{position:absolute;left:66px;top:26px;width:420px;font-style:italic;font-size:14px;line-height:22px;color:var(--text)}
.testimonial-name{position:absolute;left:879px;top:327px;font-family:var(--serif);font-size:15px;color:var(--ink)}

/* newsletter */
.newsletter{position:absolute;left:0;top:1997px;width:1200px;height:76px;background:var(--dark-2);color:var(--white)}
.newsletter .label{position:absolute;left:52px;top:16px;display:flex;align-items:center;gap:12px;font-family:var(--serif);font-size:22px}
.newsletter .ring{width:46px;height:46px;border-radius:50%;border:2px solid var(--white);display:flex;align-items:center;justify-content:center}
.email-field{position:absolute;left:397px;top:21px;width:401px;height:35px;background:var(--white);color:#333;font-family:var(--serif);font-size:13px;padding:10px 12px}
.signup-btn{position:absolute;left:818px;top:21px;width:160px;height:36px;background:#d0d0d0;color:#222;font-size:17px;font-weight:700;text-align:center;line-height:36px}
.follow{position:absolute;left:996px;top:29px;font-size:15px;display:flex;align-items:center;gap:9px;white-space:nowrap}
.follow .social{display:flex;align-items:center;gap:6px}
.follow .dot{width:12px;height:12px;border-radius:50%;background:var(--white)}

/* footer */
.site-footer{position:absolute;left:0;top:2073px;width:1200px;height:220px;background:var(--black);color:var(--white)}
.contact-item{position:absolute;top:43px;display:flex;gap:14px;font-size:14.5px;line-height:23px}
.contact-item strong{font-weight:700}
.contact-item .badge{width:32px;height:32px;border-radius:50%;background:#3a3a3a;display:flex;align-items:center;justify-content:center;flex:none;margin-top:2px}
.footer-brand{position:absolute;left:900px;top:26px;width:250px;text-align:center}
.footer-brand .name{font-family:var(--serif);font-size:14px;letter-spacing:1px}
.footer-brand .copy{font-size:13.5px;line-height:18px;margin-top:12px;color:#e0e0e0}
.footer-rule{position:absolute;left:52px;top:128px;width:1096px;height:1px;background:#3b3b3b}
.disclaimer{position:absolute;left:62px;top:145px;width:1076px;text-align:center;font-size:13.3px;line-height:21px;color:#cfcfcf}
.disclaimer u{color:var(--white)}
</style>
</head>
<body>

<header class="site-header">
  <div class="brand">THE CALLOWAY<br>LAW FIRM, PLLC</div>
  <div class="vcard-btn">VISITING CARD
    <svg width="24" height="24" viewBox="0 0 24 24"><circle cx="12" cy="12" r="12" fill="#2a2a2a"/><path d="M12 6v9M8 11l4 4 4-4" stroke="#fff" stroke-width="2.2" fill="none"/></svg>
  </div>
  <div class="header-phone">
    <span class="icon-ring"><svg width="16" height="16" viewBox="0 0 24 24"><path d="M6.6 10.8a15 15 0 0 0 6.6 6.6l2.2-2.2c.3-.3.7-.4 1-.2 1.1.4 2.3.6 3.6.6.6 0 1 .4 1 1V20c0 .6-.4 1-1 1A17 17 0 0 1 3 4c0-.6.4-1 1-1h3.5c.6 0 1 .4 1 1 0 1.3.2 2.5.6 3.6.1.3 0 .7-.2 1z" fill="#fff"/></svg></span>
    (210) 555-0147
  </div>
  <nav class="main-nav">
    <span class="active" style="left:633px">HOME</span>
    <span style="left:735px">ABOUT US</span>
    <span style="left:868px">OUR EXPERTISE</span>
    <span style="left:1050px">CONTACT US</span>
  </nav>
</header>

<section class="hero" role="img" aria-label="Two climbers on a mountain ridge at sunrise, one reaching down to help the other up">
  <h1 class="hero-title">HELPING CLIENTS MANAGE RISK<br>AND ACHIEVE GOALS</h1>
  <div class="hero-arrow prev"></div>
  <div class="hero-arrow next"></div>
  <svg class="abs" style="left:3px;top:228px" width="12" height="16" viewBox="0 0 12 16"><path d="M9 2L3 8l6 6" stroke="#222" stroke-width="2.5" fill="none"/></svg>
  <svg class="abs" style="right:3px;top:228px" width="12" height="16" viewBox="0 0 12 16"><path d="M3 2l6 6-6 6" stroke="#222" stroke-width="2.5" fill="none"/></svg>
</section>

<section class="welcome">
  <h2 class="section-title" style="top:60px">WELCOME TO THE CALLOWAY LAW FIRM <small>PLLC</small></h2>
  <div class="divider" style="left:453px;top:119px;width:296px"></div>
  <p>Client focused. Detail Oriented. Determined. The Calloway Law Firm, PLLC works tirelessly to build relationships with their clients to better understand their needs, desires, problems, risks and dreams.&nbsp; Building on an in depth understanding of the clients’needs, The Calloway Law Firm, PLLC provides each client, the personal attention that they deserve.</p>
  <div class="btn-more">READ MORE
    <span class="chev"><svg width="12" height="14" viewBox="0 0 12 14"><path d="M3 2l5 5-5 5" stroke="#222" stroke-width="2.4" fill="none"/></svg></span>
  </div>
</section>

<section class="expertise">
  <h2 class="section-title">OUR EXPERTISE</h2>
  <div class="divider" style="left:530px;top:126px;width:138px"></div>

  <article class="service" style="left:52px">
    <div class="service-photo" role="img" aria-label="Advisor shaking hands with a senior couple at a desk" style="background:linear-gradient(135deg,#e9eef2,#c9d3db 55%,#8fa0ae)"></div>
    <h3>ESTATE PLANNING</h3>
    <p>The Calloway Law Firm is dedicated to helping its clients plan for the future and for the unexpected.</p>
    <div class="plus"><svg width="12" height="12" viewBox="0 0 12 12"><path d="M6 1v10M1 6h10" stroke="#222" stroke-width="2.4"/></svg></div>
  </article>

  <article class="service" style="left:330px">
    <div class="service-photo" role="img" aria-label="Courtroom interior with wooden benches and brass scales on a table" style="background:linear-gradient(180deg,#4a2a18,#7a4626 55%,#2e1a0f)"></div>
    <h3>LITIGATION</h3>
    <p>The Calloway Law Firm has extensive experience handling cases of serious personal injury and wrongful death.</p>
    <div class="plus"><svg width="12" height="12" viewBox="0 0 12 12"><path d="M6 1v10M1 6h10" stroke="#222" stroke-width="2.4"/></svg></div>
  </article>

  <article class="service" style="left:608px">
    <div class="service-photo" role="img" aria-label="Two businessmen in suits reviewing documents at an office table" style="background:linear-gradient(135deg,#dfe6ee,#7d93ab 55%,#2f3f55)"></div>
    <h3>BUSINESS PLANNING<br>&amp; LITIGATION</h3>
    <p>The Firm is experienced in litigating cases involving breach of contract, Deceptive Trade Practices Act.</p>
    <div class="plus"><svg width="12" height="12" viewBox="0 0 12 12"><path d="M6 1v10M1 6h10" stroke="#222" stroke-width="2.4"/></svg></div>
  </article>

  <article class="service" style="left:888px">
    <div class="service-photo" role="img" aria-label="Business team around a meeting table shaking hands" style="background:linear-gradient(135deg,#eef2f4,#b7c4cc 50%,#5b6670)"></div>
    <h3>MEDIATION</h3>
    <p>Evelyn is a certified mediator offering both full and half day mediations. Please call or email for more information.</p>
    <div class="plus"><svg width="12" height="12" viewBox="0 0 12 12"><path d="M6 1v10M1 6h10" stroke="#222" stroke-width="2.4"/></svg></div>
  </article>
</section>

<section class="proof">
  <div class="col-head" style="left:52px">
    <svg width="26" height="32" viewBox="0 0 26 32"><rect x="2" y="4" width="20" height="26" fill="none" stroke="#222" stroke-width="2"/><rect x="7" y="1" width="10" height="6" fill="#222"/><path d="M6 13h12M6 18h12M6 23h8" stroke="#222" stroke-width="2"/></svg>
    RESULTS
  </div>
  <div class="pager" style="left:499px">
    <span><svg width="8" height="12" viewBox="0 0 8 12"><path d="M6 1L1 6l5 5" stroke="#333" stroke-width="1.6" fill="none"/></svg></span>
    <span><svg width="8" height="12" viewBox="0 0 8 12"><path d="M2 1l5 5-5 5" stroke="#333" stroke-width="1.6" fill="none"/></svg></span>
  </div>
  <div class="divider" style="left:52px;top:129px;width:521px"></div>
  <p class="results-text"><strong>Marisol Delgado v. Brackett Oilfield Services</strong> (Uvalde District Court)In this oil field services personal injury case, Evelyn L. Calloway successfully argued summary judgment against a well known State Representative on behalf of her client thereby obtaining a dismissal of all claims of gross negligence.</p>

  <div class="col-head" style="left:634px">
    <svg width="26" height="24" viewBox="0 0 26 24"><path d="M2 2h15v10H8l-4 4v-4H2z" fill="#222"/><path d="M19 7h5v10h-2v4l-4-4h-7v-3h8z" fill="#222"/></svg>
    CLIENT TESTIMONIALS
  </div>
  <div class="pager" style="left:1081px">
    <span><svg width="8" height="12" viewBox="0 0 8 12"><path d="M6 1L1 6l5 5" stroke="#333" stroke-width="1.6" fill="none"/></svg></span>
    <span><svg width="8" height="12" viewBox="0 0 8 12"><path d="M2 1l5 5-5 5" stroke="#333" stroke-width="1.6" fill="none"/></svg></span>
  </div>
  <div class="divider" style="left:634px;top:129px;width:514px"></div>
  <div class="testimonial">
    <svg width="510" height="190" viewBox="0 0 510 190"><path d="M10 1h490a9 9 0 0 1 9 9v132a9 9 0 0 1-9 9H440l-74 20 16-20H10a9 9 0 0 1-9-9V10a9 9 0 0 1 9-9z" fill="#fff" stroke="#c8c8c8" stroke-width="1.5"/></svg>
    <span class="quote-mark">“</span>
    <p>I want to express my sincere thanks and appreciation….&nbsp; I know you put your valuable time and professional effort into working for me but also to counsel through best options while navigating through this case. Thank you very much.</p>
  </div>
  <div class="testimonial-name">Daniel R., PT</div>
</section>

<section class="newsletter">
  <div class="label">
    <span class="ring"><svg width="22" height="16" viewBox="0 0 22 16"><rect x="1" y="1" width="20" height="14" fill="#fff"/><path d="M1 1l10 8 10-8" stroke="#333" stroke-width="1.6" fill="none"/></svg></span>
    NEWSLETTER SIGNUP
    <svg width="18" height="44" viewBox="0 0 18 44"><path d="M2 2l14 20-14 20" stroke="#fff" stroke-width="1.5" fill="none"/></svg>
  </div>
  <div class="email-field">Your e-mail</div>
  <div class="signup-btn">SIGN UP</div>
  <div class="follow">FOLLOW US :
    <span class="social"><span class="dot"></span>Chatterly</span>
  </div>
</section>

<footer class="site-footer">
  <div class="contact-item" style="left:54px">
    <span class="badge"><svg width="12" height="16" viewBox="0 0 12 16"><path d="M6 0a6 6 0 0 0-6 6c0 4.5 6 10 6 10s6-5.5 6-10a6 6 0 0 0-6-6z" fill="#fff"/><circle cx="6" cy="6" r="2.2" fill="#3a3a3a"/></svg></span>
    <div><strong>The Calloway Law Firm, PLLC</strong><br>18420 IH-10 West, Suite 305-120<br>San Antonio, Texas 78257</div>
  </div>
  <div class="contact-item" style="left:371px">
    <span class="badge"><svg width="14" height="14" viewBox="0 0 24 24"><path d="M6.6 10.8a15 15 0 0 0 6.6 6.6l2.2-2.2c.3-.3.7-.4 1-.2 1.1.4 2.3.6 3.6.6.6 0 1 .4 1 1V20c0 .6-.4 1-1 1A17 17 0 0 1 3 4c0-.6.4-1 1-1h3.5c.6 0 1 .4 1 1 0 1.3.2 2.5.6 3.6.1.3 0 .7-.2 1z" fill="#fff"/></svg></span>
    <div><strong>Call Us :</strong><br>(210) 555-0147</div>
  </div>
  <div class="contact-item" style="left:577px">
    <span class="badge"><svg width="14" height="11" viewBox="0 0 22 16"><rect x="1" y="1" width="20" height="14" fill="#fff"/><path d="M1 1l10 8 10-8" stroke="#3a3a3a" stroke-width="1.8" fill="none"/></svg></span>
    <div><strong>Email Us :</strong><br>admin@callowaylawfirm.com</div>
  </div>
  <div class="footer-brand">
    <div class="name">THE CALLOWAY LAW FIRM</div>
    <div class="copy">© 2016 The Calloway Law Firm, PLLC.<br>All Rights Reserved.</div>
  </div>
  <div class="footer-rule"></div>
  <p class="disclaimer"><u>Disclaimer:</u> The information you obtain at this site is not, nor is it intended to be, legal advice. You should consult an attorney for advice regarding your individual situation. We invite you to contact us and welcome your calls, letters and electronic mail. Contacting us does not create an attorney-client relationship. Also, please note any past results is not a guarantee of any future results.&nbsp; Please do not send any confidential information to us until such time as an attorney-client relationship has been established.</p>
</footer>

</body>
</html>
```